I need a direct mail postcard made up for my marketing campaign

I am starting a marketing campaign and need a design for a post card. I own an iron door company and need to have before and after images on the post card to showcase what our work looks like. I have provided pictures to use below.

The design needs to be two sided. The logo should be on the front.

The tag line for this campaign is: Design the smile your home deserves.

Words to also use: Distinctive style, Work of Art, One-of-a-Kind, Elegant, Modern, Innovative, Unique

My information for the card
Name: Dean Harlowe
Phone number: (555)-318-2764
Email: Dean@wroughtgatestudio.example

The US postal system is very picky as to what can be sent in the mail. The only requirement they have is for the address. There needs to be a 2inch (50.8mm) by 4inch (101.6mm) blank space on the bottom right hand corner on the back of the card.

Target Market(s)

Home owners

Industry/Entity Type

Home Improvement

Font styles to use
Serif
Decorative

Colors
0555a3
ffffff
ec1f27

Requirements
Must have
• My logo, My contact information, before and after pictures
• Provided 3D images
Nice to have
• Words that describe iron doors
• A contrast between contemporary and ornate doors.

```html
<!DOCTYPE html>
<html lang="en">
<head>
<meta charset="utf-8">
<title>Wrought Gate Studio – Postcard Front</title>
<link rel="stylesheet" href="https://fonts.googleapis.com/css2?family=Kaushan+Script&family=Open+Sans:wght@700;800&family=Roboto+Condensed:ital,wght@0,700;1,700&display=swap">
<style>
  :root {
    --brand-blue: #0555a3;
    --brand-red: #ec1f27;
    --white: #ffffff;
    --ink: #111111;
    --orange-deep: #e2601c;
    --orange-mid: #f08a3a;
    --cream: #fde9c4;
    --band-dark: #2b2b2b;
  }
  * { margin: 0; padding: 0; box-sizing: border-box; }
  html, body { width: 1200px; height: 776px; overflow: hidden; background: #ffffff; }
  .postcard {
    position: relative;
    width: 1200px;
    height: 776px;
    overflow: hidden;
    background:
      radial-gradient(ellipse 520px 420px at 860px 330px, var(--cream) 0%, #f9c98a 45%, rgba(240,138,58,0) 100%),
      linear-gradient(100deg, var(--orange-deep) 0%, var(--orange-mid) 55%, #f6b26b 100%);
  }
  .backdrop { position: absolute; inset: 0; }
  .door-photo {
    position: absolute;
    left: 12px;
    top: 44px;
    width: 604px;
    height: 586px;
    background: var(--white);
    padding: 10px;
    transform: rotate(-2.4deg);
    box-shadow: 0 4px 12px rgba(0,0,0,0.25);
  }
  .door-photo__fill {
    width: 100%;
    height: 100%;
    background:
      linear-gradient(90deg, #c89a4a 0%, #6e3b2c 18%, #5a3a3a 50%, #6e3b2c 82%, #c89a4a 100%);
  }
  .headline {
    position: absolute;
    left: 600px;
    width: 528px;
    top: 82px;
    text-align: center;
    font-family: "Kaushan Script", cursive;
    font-size: 58px;
    line-height: 62px;
    color: var(--brand-blue);
  }
  .brand-name {
    position: absolute;
    left: 700px;
    width: 320px;
    top: 300px;
    text-align: center;
    font-family: "Open Sans", sans-serif;
    font-weight: 800;
    font-size: 28px;
    line-height: 34px;
    color: var(--brand-blue);
    text-transform: uppercase;
  }
  .contact {
    position: absolute;
    left: 620px;
    width: 484px;
    text-align: center;
    color: var(--ink);
    font-family: "Open Sans", sans-serif;
    font-weight: 700;
  }
  .contact--phone { top: 446px; font-size: 31px; }
  .contact--email { top: 494px; font-size: 21px; }
  .slogan, .cta {
    position: absolute;
    left: 620px;
    width: 484px;
    text-align: center;
    font-family: "Roboto Condensed", sans-serif;
    font-weight: 700;
    text-transform: uppercase;
  }
  .slogan { top: 538px; font-size: 22px; color: var(--brand-blue); }
  .cta { top: 570px; font-size: 20px; color: var(--ink); }
  .social {
    position: absolute;
    top: 618px;
    left: 802px;
    display: flex;
    gap: 8px;
  }
  .social__dot {
    width: 34px;
    height: 34px;
    border-radius: 50%;
    background: var(--brand-red);
  }
  .social__dot--blue { background: var(--brand-blue); }
  .qualities {
    position: absolute;
    left: 0;
    width: 1200px;
    top: 704px;
    text-align: center;
    font-family: "Roboto Condensed", sans-serif;
    font-style: italic;
    font-weight: 700;
    font-size: 26px;
    color: var(--white);
    text-transform: uppercase;
    letter-spacing: 0.2px;
  }
</style>
</head>
<body>
<div class="postcard">
  <svg class="backdrop" width="1200" height="776" viewBox="0 0 1200 776" aria-hidden="true">
    <defs>
      <linearGradient id="bandShade" x1="0" y1="0" x2="1" y2="0">
        <stop offset="0" stop-color="#ec1f27"/>
        <stop offset="0.18" stop-color="#3a2b2b"/>
        <stop offset="0.5" stop-color="#2b2b2b"/>
        <stop offset="0.75" stop-color="#4a2424"/>
        <stop offset="1" stop-color="#ec1f27"/>
      </linearGradient>
    </defs>
    <path class="wave-red" d="M560,700 C780,660 980,610 1200,590 L1200,776 L560,776 Z" fill="#ec1f27"/>
    <path class="band-dark" d="M0,690 C260,720 520,700 760,666 C940,640 1080,628 1200,622 L1200,776 L0,776 Z" fill="url(#bandShade)"/>
    <path class="wave-white" d="M0,668 C240,708 520,692 760,656 C930,632 1080,622 1200,616 L1200,626 C1080,634 940,648 760,674 C520,708 250,724 0,692 Z" fill="#ffffff"/>
    <path class="wave-blue" d="M0,640 C250,690 520,680 760,646 C900,626 1060,616 1200,612 L1200,620 C1060,626 920,640 760,664 C520,700 250,712 0,676 Z" fill="#0555a3"/>
  </svg>

  <div class="door-photo">
    <div class="door-photo__fill" role="img" aria-label="Photo of an ornate bronze double iron entry door with scrollwork, flanked by topiary plants in gold urns"></div>
  </div>

  <h1 class="headline">Design the smile your<br>home deserves</h1>

  <div class="brand-name">Wrought Gate<br>Studio</div>

  <p class="contact contact--phone">(555)-318-2764</p>
  <p class="contact contact--email">Dean@wroughtgatestudio.example</p>
  <p class="slogan">Your memories, your heart, your home!</p>
  <p class="cta">Call or text for free estimate</p>

  <div class="social" aria-label="Social media">
    <span class="social__dot social__dot--blue"></span>
    <span class="social__dot"></span>
    <span class="social__dot"></span>
  </div>

  <p class="qualities">Distinctive Style | Work of Art | One-of-a-Kind | Elegant | Modern | Innovative | Unique</p>
</div>
</body>
</html>
```